Business Card for Polygraph business in Africa

Business Card . Polygraph Examiner based in Tanzania, East Africa.
Business Card will be used to disseminate contact information to potential clients.
It should convey that I am a professional specifically in the polygraph field and perform my work with integrity.

I have attached the business card that I'm currently using, which I threw together myself initially. It's not professional enough.

Target Market(s)

Banks, Accounting Firms, Government Ministries, Gas, Oil, & Gemstone Mining Concerns, Wildlife Conservation NGOs, International companies located in East Africa.

Industry/Entity Type

Business

Contact Information for Business Card

Veritas Lumeno
Harriet Munsell
PO Box 48317
Arusha, Tanzania
+255 712 839 254
harrietmunsell@quillpost.example

Colors
00a990
f37122
faa54b

Requirements
Must have
• - Veritas Lumeno (with the word "Polygraph" being more prominent than the word "Tanzania")
• - Forensic Examinations
• - Employment Screening
• - Should contain a logo of the Continental Truthfinder Guild (of which I'm a member)
• - I would like an accent design (such as the polygraph "squiggles" of a cardio tracing or such as that)
• - My contact information (less prominent, but large enough to read legibly). I would also consider putting the contact information on the second side of the card.
Nice to have
• My color suggestions are changeable.
Should not have
• Anything "cutesy" or "cartoonish"

```html
<!DOCTYPE html>
<html lang="en">
<head>
<meta charset="utf-8">
<title>Veritas Lumeno – Business Card</title>
<link href="https://fonts.googleapis.com/css2?family=Roboto:wght@400;500;700&family=Roboto+Condensed:wght@400;700&display=swap" rel="stylesheet">
<style>
  :root {
    --brand-blue: #0a4ea3;
    --brand-blue-deep: #08438e;
    --card-white: #f7f8fa;
    --ink: #3b3f46;
    --trace-faint: #dfe4ec;
    --stage: #e9e7e2;
  }
  * { box-sizing: border-box; margin: 0; padding: 0; }
  html, body { width: 1200px; height: 911px; overflow: hidden; }
  body {
    background: var(--stage);
    font-family: "Roboto", Arial, sans-serif;
    display: flex;
    align-items: center;
    justify-content: center;
    gap: 40px;
  }
  .card {
    position: relative;
    width: 540px;
    height: 309px;
    border-radius: 18px;
    overflow: hidden;
    box-shadow: 0 10px 28px rgba(0,0,0,0.18);
  }

  /* Front */
  .card-front { background: var(--card-white); }
  .front-band {
    position: absolute; left: 0; top: 0; bottom: 0;
    width: 58px; background: var(--brand-blue);
  }
  .front-decor {
    position: absolute; right: 40px; top: 70px;
    width: 190px; height: 190px; border-radius: 50%;
    background: var(--trace-faint); opacity: 0.7;
  }
  .guild-badge {
    position: absolute; right: 26px; top: 20px;
    width: 58px; height: 58px; border-radius: 50%;
    background: #e8e9f4; border: 3px solid #4a4fa6;
  }
  .brand {
    position: absolute; left: 30px; top: 28px;
    display: flex; align-items: center; gap: 12px;
  }
  .brand-dot {
    width: 56px; height: 56px; border-radius: 50%;
    background: var(--card-white); border: 4px solid var(--brand-blue);
  }
  .brand-name {
    font-family: "Roboto Condensed", Arial Narrow, sans-serif;
    font-weight: 700; font-size: 30px; color: var(--brand-blue);
    letter-spacing: 0.2px;
  }
  .contact {
    position: absolute; left: 88px; top: 118px;
    font-family: "Roboto Condensed", Arial Narrow, sans-serif;
    color: var(--ink); font-size: 15px; line-height: 1.3;
  }
  .contact-name { color: var(--brand-blue); font-weight: 700; font-size: 19px; }
  .contact-company { font-size: 15px; margin-bottom: 10px; }
  .contact-line { display: flex; align-items: center; gap: 8px; }
  .contact-line svg { width: 12px; height: 12px; fill: var(--brand-blue); flex: none; }
  .address { margin-bottom: 6px; }

  /* Back */
  .card-back { background: var(--brand-blue); color: #fff; }
  .back-mark {
    position: absolute; left: 50%; top: 44%;
    transform: translate(-50%, -50%);
    display: flex; flex-direction: column; align-items: center; gap: 12px;
  }
  .back-ring {
    width: 110px; height: 110px; border-radius: 50%;
    border: 6px solid #fff;
  }
  .back-name {
    font-family: "Roboto Condensed", Arial Narrow, sans-serif;
    font-weight: 700; font-size: 24px;
  }
  .tagline {
    position: absolute; left: 30px; bottom: 24px;
    font-size: 14px; font-style: normal; letter-spacing: 0.3px;
    display: flex; align-items: center; gap: 10px;
  }
  .tagline-dot { width: 6px; height: 6px; border-radius: 50%; background: #fff; }
</style>
</head>
<body>
  <section class="card card-front" aria-label="Card front">
    <div class="front-band"></div>
    <div class="front-decor" aria-hidden="true"></div>
    <div class="guild-badge" role="img" aria-label="Continental Truthfinder Guild membership badge"></div>
    <div class="brand">
      <div class="brand-dot" aria-hidden="true"></div>
      <div class="brand-name">Veritas Lumeno</div>
    </div>
    <div class="contact">
      <div class="contact-name">HARRIET MUNSELL</div>
      <div class="contact-company">VERITAS LUMENO</div>
      <div class="address">PO Box 48317<br>Arusha, Tanzania</div>
      <div class="contact-line">
        <svg viewBox="0 0 24 24"><path d="M6.6 10.8a15 15 0 0 0 6.6 6.6l2.2-2.2a1 1 0 0 1 1-.25 11.4 11.4 0 0 0 3.6.57 1 1 0 0 1 1 1V20a1 1 0 0 1-1 1A17 17 0 0 1 3 4a1 1 0 0 1 1-1h3.5a1 1 0 0 1 1 1c0 1.25.2 2.45.57 3.57a1 1 0 0 1-.25 1z"/></svg>
        +255 712 839 254
      </div>
      <div class="contact-line">
        <svg viewBox="0 0 24 24"><path d="M2 5h20v14H2z M2 5l10 8 10-8" fill="none" stroke="#0a4ea3" stroke-width="2.5"/></svg>
        harrietmunsell@quillpost.example
      </div>
      <div class="contact-line">
        <svg viewBox="0 0 24 24"><circle cx="12" cy="12" r="10"/></svg>
        www.harrietmunsell.example
      </div>
    </div>
  </section>

  <section class="card card-back" aria-label="Card back">
    <div class="back-mark">
      <div class="back-ring" aria-hidden="true"></div>
      <div class="back-name">Veritas Lumeno</div>
    </div>
    <div class="tagline">
      <span>Forensic Examinations</span>
      <span class="tagline-dot" aria-hidden="true"></span>
      <span>Employment Screening</span>
    </div>
  </section>
</body>
</html>
```